Educate
Education
Creative Brief
It an educational site, N.G.O
Likes: Green White Green
above header
http://brevardlearning.org/
http://www.koltrex.org/offices/education/about/index.html

```html
<!DOCTYPE html>
<html lang="en">
<head>
<meta charset="utf-8">
<title>Brightpath Learning</title>
<link rel="stylesheet" href="https://fonts.googleapis.com/css2?family=Tinos:ital,wght@0,400;0,700;1,700&family=Arimo:wght@700&display=swap">
<style>
:root{
  --green-dark:#0b5a2c;
  --green:#12773a;
  --green-mid:#1f8f47;
  --green-light:#3aa85e;
  --panel-grey:#e4e6e4;
  --tab-grey:#d9dcd9;
  --text-dark:#1d2a20;
  --field-border:#9aa39c;
  --alert-red:#d3231f;
  --orange:#e8581c;
  --white:#ffffff;
}
*{box-sizing:border-box;margin:0;padding:0}
html,body{width:1200px;height:715px;overflow:hidden}
body{position:relative;background:var(--white);font-family:"Tinos",serif;color:var(--text-dark)}
.top-rule{position:absolute;left:0;top:0;width:1200px;height:6px;background:var(--green)}
.bottom-band{position:absolute;left:0;top:703px;width:1200px;height:12px;background:var(--green)}
.brand{position:absolute;left:144px;top:30px;display:flex;align-items:center;gap:12px}
.brand-mark{width:44px;height:44px;border-radius:50%;background:var(--green-mid)}
.brand-name{font-family:"Tinos",serif;font-weight:700;font-size:30px;line-height:1;color:var(--green);letter-spacing:1px}
.social{position:absolute;top:46px;display:block;width:36px;height:36px;border-radius:6px;background:var(--green-light)}
.social.one{left:958px}.social.two{left:1000px;background:var(--green-mid)}
.page-panel{position:absolute;left:101px;top:113px;width:998px;height:530px;border-radius:10px;background:linear-gradient(180deg,var(--green) 0%,var(--green-dark) 100%)}
.main-nav{position:absolute;left:115px;top:118px;width:979px;height:40px;display:flex}
.main-nav a{display:flex;align-items:center;justify-content:center;height:40px;color:var(--white);font-weight:700;font-size:16px;text-decoration:none;border-right:1px solid rgba(255,255,255,.25);background:linear-gradient(180deg,var(--green-light),var(--green))}
.main-nav a.active{background:var(--tab-grey);color:var(--green-dark)}
.hero{position:absolute;left:108px;top:161px;width:737px;height:283px;background:linear-gradient(120deg,#2f5a3a 0%,#8c6a4a 35%,#b8a88f 60%,#4e5a63 100%)}
.hero-caption{position:absolute;left:138px;top:352px;font-family:"Arimo",sans-serif;font-weight:700;font-size:32px;line-height:38px;color:var(--white);text-shadow:2px 2px 3px rgba(0,0,0,.7)}
.hero-caption span{display:block}
.hero-caption span+span{padding-left:32px}
.quick-contact{position:absolute;left:852px;top:161px;width:242px;height:283px;background:var(--panel-grey)}
.qc-head{height:34px;display:flex;align-items:center;gap:10px;padding-left:14px;border-bottom:2px solid var(--green);background:linear-gradient(180deg,#f4f5f4,#d6dad6)}
.qc-head svg{width:22px;height:22px}
.qc-head h2{font-size:15px;font-weight:700;color:var(--green-dark);letter-spacing:.5px}
.qc-row{position:absolute;left:10px;font-size:13px;font-weight:700;color:var(--green-dark)}
.qc-field{position:absolute;left:72px;width:162px;height:22px;background:var(--white);border:1px solid var(--field-border)}
.qc-field.area{height:62px}
.qc-submit{position:absolute;left:76px;top:234px;width:118px;height:30px;border-radius:4px;background:linear-gradient(180deg,var(--green-light),var(--green-dark));color:var(--white);font-weight:700;font-size:14px;display:flex;align-items:center;justify-content:center}
.feature{position:absolute;top:451px;width:235px;height:178px;background:var(--white)}
.feature h3{height:36px;display:flex;align-items:center;justify-content:center;font-style:italic;font-weight:700;font-size:15px;color:var(--green);background:linear-gradient(180deg,#f7f8f7,#d3d7d3);border-bottom:2px solid var(--green)}
.feature .photo{position:absolute;left:4px;top:40px;width:227px;height:134px}
.f1{left:108px}.f2{left:360px}.f3{left:612px}
.f1 .photo{background:linear-gradient(135deg,#c8d2d8,#6a7d8c)}
.f2 .photo{background:linear-gradient(180deg,#7fa6c8 0%,#5c8a3a 60%,#3e6a2a 100%)}
.f3 .photo{background:linear-gradient(135deg,#d9d2c4,#7a5a44)}
.donate-card{position:absolute;left:852px;top:451px;width:242px;height:178px;background:linear-gradient(135deg,#5a6a3a,#8a6a4a 55%,#3a3a2c)}
.donate-badge{position:absolute;left:12px;top:76px;width:80px;height:80px;border-radius:50%;background:var(--orange);border:3px solid var(--white);display:flex;flex-direction:column;align-items:center;justify-content:center;color:var(--white);font-weight:700;font-size:16px;line-height:17px}
.copyright{position:absolute;left:115px;top:666px;font-size:14px;color:var(--green-dark)}
.footer-nav{position:absolute;left:790px;top:664px;display:flex;gap:12px;font-size:14px;color:var(--green-dark)}
.footer-nav a{color:var(--green-dark);text-decoration:none}
</style>
</head>
<body>
<div class="top-rule"></div>

<header class="brand">
  <span class="brand-mark"></span>
  <span class="brand-name">BRIGHTPATH LEARNING</span>
</header>
<span class="social one"></span>
<span class="social two"></span>

<div class="page-panel"></div>

<nav class="main-nav">
  <a href="#" style="width:84px">Home</a>
  <a href="#" class="active" style="width:132px">About Us</a>
  <a href="#" style="width:132px">Services</a>
  <a href="#" style="width:168px">News &amp; Events</a>
  <a href="#" style="width:168px">Make Donation</a>
  <a href="#" style="width:156px">Testimonials</a>
  <a href="#" style="width:139px;border-right:0">Contact Us</a>
</nav>

<div class="hero" role="img" aria-label="Students studying in a library with a smiling teacher"></div>
<p class="hero-caption"><span>We Will Help You to</span><span>Understand&nbsp; the world</span></p>

<aside class="quick-contact">
  <div class="qc-head">
    <svg viewBox="0 0 22 22" aria-hidden="true"><path d="M6 3c2 0 3 4 2 5l-1 1c1 2 3 4 5 5l1-1c1-1 5 0 5 2 0 2-2 4-4 4C8 19 3 14 3 7c0-2 1-4 3-4z" fill="var(--alert-red)"/></svg>
    <h2>QUICK CONTACT</h2>
  </div>
  <span class="qc-row" style="top:48px">Name :</span><span class="qc-field" style="top:44px"></span>
  <span class="qc-row" style="top:86px">Phone :</span><span class="qc-field" style="top:82px"></span>
  <span class="qc-row" style="top:123px">Email :</span><span class="qc-field" style="top:119px"></span>
  <span class="qc-row" style="top:164px">Message :</span><span class="qc-field area" style="top:158px"></span>
  <span class="qc-submit">SUBMIT</span>
</aside>

<section class="feature f1"><h3>EDUCATORS</h3><div class="photo" role="img" aria-label="Teacher helping pupils at computers"></div></section>
<section class="feature f2"><h3>FAMILIES</h3><div class="photo" role="img" aria-label="Family relaxing together on grass outdoors"></div></section>
<section class="feature f3"><h3>FOR STUDENTS</h3><div class="photo" role="img" aria-label="Group of smiling students"></div></section>
<section class="donate-card" role="img" aria-label="Child drinking from a bowl">
  <span class="donate-badge"><span>Donate</span><span>Now</span></span>
</section>

<p class="copyright">Copyright © 2010-2011, BRIGHTPATH LEARNING</p>
<nav class="footer-nav">
  <a href="#">Home</a><span>|</span><a href="#">About Us</a><span>|</span><a href="#">Services</a><span>|</span><a href="#">Contact Us</a>
</nav>

<div class="bottom-band"></div>
</body>
</html>
```